corvanel antique auction

traditional auction house website. example : brackwoodauction.com, marrowbyinc.com, corinnevaltby.com

Industry/Entity Type

House

Number of Pages Required

5+ page

```html
<!DOCTYPE html>
<html lang="en">
<head>
<meta charset="utf-8">
<title>Corvanel Antique Auction</title>
<link href="https://fonts.googleapis.com/css2?family=Open+Sans:ital,wght@0,300;0,400;0,600;0,700;1,400;1,600&display=swap" rel="stylesheet">
<style>
:root{
  --teal:#23868a;
  --teal-tab:#3a9c9e;
  --teal-tab-dark:#2f8f91;
  --ink:#2b2b2b;
  --muted:#6f6f6f;
  --soft:#8a8a8a;
  --line:#d9d9d9;
  --tab:rgba(38,40,48,.92);
  --tab-dark:rgba(30,32,38,.95);
  --white:#ffffff;
}
*{margin:0;padding:0;box-sizing:border-box}
html,body{width:944px;height:1200px;overflow:hidden;background:var(--white)}
body{position:relative;font-family:'Open Sans',sans-serif;color:var(--ink)}
.abs{position:absolute}

/* header */
.site-header{position:absolute;left:0;top:0;width:944px;height:49px;border-bottom:1px solid #c9c9c9;background:var(--white)}
.brand{position:absolute;left:22px;top:13px;font-size:16px;font-weight:400;color:var(--teal);white-space:nowrap}
.main-nav a,.account a{position:absolute;top:19px;font-size:10px;color:#444;text-decoration:none;white-space:nowrap}
.caret{display:inline-block;width:4px;height:4px;border-right:1px solid #666;border-bottom:1px solid #666;transform:rotate(45deg);margin-left:6px;vertical-align:2px}
.cart-icon{position:absolute;left:808px;top:15px}
.cart-text{position:absolute;left:830px;top:19px;font-size:10px;color:#444;white-space:nowrap}

/* hero */
.hero{position:absolute;left:0;top:49px;width:944px;height:440px;
  background:linear-gradient(180deg,#b9b6a8 0%,#a9a38f 35%,#9c9784 60%,#7d7566 100%)}
.hero-next{position:absolute;left:896px;top:261px;width:22px;height:22px;border-radius:50%;background:rgba(0,0,0,.12)}
.tabs{position:absolute;left:78px;top:389px;width:789px;height:100px;display:flex}
.tab{position:relative;width:197.25px;height:100px;background:var(--tab);color:var(--white);border-left:1px solid rgba(255,255,255,.08)}
.tab.is-active{background:var(--teal-tab)}
.tab .arrow-cell{position:absolute;right:0;top:0;width:48px;height:65px;background:var(--tab-dark)}
.tab.is-active .arrow-cell{background:var(--teal-tab-dark)}
.tab .arrow-cell svg{position:absolute;left:18px;top:14px}
.tab .kicker{position:absolute;left:19px;top:12px;font-size:13.5px;font-weight:400}
.tab .title{position:absolute;left:19px;top:28px;font-size:24px;font-weight:300}
.tab .count,.tab .more{position:absolute;top:77px;font-size:9px;font-style:italic}
.tab .count{left:19px}
.tab .more{right:14px}
.tab:not(.is-active) .count,.tab:not(.is-active) .more,.tab:not(.is-active) .arrow-cell svg{opacity:.45}

/* latest */
.section-title{position:absolute;left:78px;top:524px;font-size:13px;font-weight:700;letter-spacing:.3px;color:#222}
.lot{position:absolute;width:187px}
.lot .photo{width:187px;height:122px}
.lot .name{margin-top:14px;text-align:center;font-size:9px;font-weight:700;color:#333;letter-spacing:.2px}
.lot .link{margin-top:8px;text-align:center;font-size:8.5px;font-style:italic;color:var(--soft)}

/* footer */
.rule{position:absolute;left:0;width:941px;height:1px;background:var(--line)}
.foot-h{position:absolute;top:990px;font-size:9.5px;font-weight:700;color:#333;letter-spacing:.2px}
.foot-list{position:absolute;top:1012px;list-style:none}
.foot-list li{font-size:8.5px;color:var(--muted);line-height:17.5px}
.foot-copy{position:absolute;font-size:8.5px;color:var(--muted);line-height:14px}
.email{position:absolute;left:418px;top:1053px;width:181px;height:26px;border:1px solid #c8c8c8}
.email span{position:absolute;left:9px;top:7px;font-size:8.5px;color:#777}
.email svg{position:absolute;right:8px;top:8px}
.social{position:absolute;display:flex;align-items:center;font-size:8.5px;color:var(--muted)}
.social i{display:block;width:27px;height:27px;border-radius:50%;margin-right:5px}
.copyright{position:absolute;top:1159px;left:0;width:944px;text-align:center;font-size:8.5px;color:var(--muted)}
</style>
</head>
<body>

<header class="site-header">
  <div class="brand">Corvanel Antique Auction</div>
  <nav class="main-nav">
    <a style="left:235px">Auctions<span class="caret"></span></a>
    <a style="left:322px">Sell &amp; Buy<span class="caret"></span></a>
    <a style="left:415px">Specialists<span class="caret"></span></a>
    <a style="left:510px">Services<span class="caret"></span></a>
    <a style="left:597px">Inside<span class="caret"></span></a>
  </nav>
  <div class="account"><a style="left:729px">My Account<span class="caret"></span></a></div>
  <svg class="cart-icon" width="16" height="18" viewBox="0 0 16 18"><path d="M1.5 5.5h13v11.5h-13z M5 5.5V3.5a3 3 0 0 1 6 0v2" fill="none" stroke="#777" stroke-width="1"/></svg>
  <div class="cart-text">Your cart is : 0 Items</div>
</header>

<section class="hero" role="img" aria-label="Bedroom furnished with antiques: upholstered bed, lamps, mirrored chest, carved mirror and bench">
  <div class="hero-next"></div>
</section>

<div class="tabs">
  <div class="tab is-active">
    <div class="kicker">Featured</div><div class="title">Auction</div>
    <div class="arrow-cell"><svg width="12" height="36" viewBox="0 0 12 36"><path d="M1 1l10 17-10 17" fill="none" stroke="#fff" stroke-width="1"/></svg></div>
    <div class="count">390 Products Available</div><div class="more">Click here</div>
  </div>
  <div class="tab">
    <div class="kicker">Recent</div><div class="title">Auction</div>
    <div class="arrow-cell"><svg width="12" height="36" viewBox="0 0 12 36"><path d="M1 1l10 17-10 17" fill="none" stroke="#fff" stroke-width="1"/></svg></div>
    <div class="count">390 Products Available</div><div class="more">Click here</div>
  </div>
  <div class="tab">
    <div class="kicker">Upcoming</div><div class="title">Auction</div>
    <div class="arrow-cell"><svg width="12" height="36" viewBox="0 0 12 36"><path d="M1 1l10 17-10 17" fill="none" stroke="#fff" stroke-width="1"/></svg></div>
    <div class="count">390 Products Available</div><div class="more">Click here</div>
  </div>
  <div class="tab">
    <div class="kicker">Meet our</div><div class="title">Specialists</div>
    <div class="arrow-cell"><svg width="12" height="36" viewBox="0 0 12 36"><path d="M1 1l10 17-10 17" fill="none" stroke="#fff" stroke-width="1"/></svg></div>
    <div class="count">390 Products Available</div><div class="more">Click here</div>
  </div>
</div>

<h2 class="section-title">LATEST AUCTION</h2>

<div class="lot" style="left:78px;top:563px"><div class="photo" role="img" aria-label="White ceramic vases beside a wooden picture frame" style="background:linear-gradient(135deg,#e7e4df,#cfc8bf 60%,#a86a4a)"></div><div class="name">LOREM IPSUM IS SIMPLY DUMMY</div><div class="link">Click here for view details</div></div>
<div class="lot" style="left:278px;top:563px"><div class="photo" role="img" aria-label="Patterned grey and white cushions on a bed" style="background:linear-gradient(135deg,#6e6e70,#b9b8b6 50%,#dcdad6)"></div><div class="name">LOREM IPSUM IS SIMPLY DUMMY</div><div class="link">Click here for view details</div></div>
<div class="lot" style="left:479px;top:563px"><div class="photo" role="img" aria-label="Sunburst electric guitar being played" style="background:linear-gradient(135deg,#3a3333,#7a4f52 50%,#5a5450)"></div><div class="name">LOREM IPSUM IS SIMPLY DUMMY</div><div class="link">Click here for view details</div></div>
<div class="lot" style="left:679px;top:563px"><div class="photo" role="img" aria-label="Carved wooden floral relief panel" style="background:linear-gradient(135deg,#3b2717,#8a6440 50%,#2e1f12)"></div><div class="name">LOREM IPSUM IS SIMPLY DUMMY</div><div class="link">Click here for view details</div></div>

<div class="lot" style="left:78px;top:754px"><div class="photo" role="img" aria-label="Antique pocket watch resting on sheet music" style="background:linear-gradient(135deg,#3d2a14,#9a7a4c 55%,#5a4220)"></div><div class="name">LOREM IPSUM IS SIMPLY DUMMY</div><div class="link">Click here for view details</div></div>
<div class="lot" style="left:278px;top:754px"><div class="photo" role="img" aria-label="Gold and enamel jewelled necklace on dark fabric" style="background:linear-gradient(135deg,#2a2e3a,#3c3f4c 55%,#7a5a2a)"></div><div class="name">LOREM IPSUM IS SIMPLY DUMMY</div><div class="link">Click here for view details</div></div>
<div class="lot" style="left:479px;top:754px"><div class="photo" role="img" aria-label="Orange leather handbag with matching high heels" style="background:linear-gradient(135deg,#f4f1ee,#c4602f 55%,#9a4520)"></div><div class="name">LOREM IPSUM IS SIMPLY DUMMY</div><div class="link">Click here for view details</div></div>
<div class="lot" style="left:679px;top:754px"><div class="photo" role="img" aria-label="Ornate carved oval mirror flanked by topiary plants" style="background:linear-gradient(135deg,#8f9490,#5a4432 50%,#9a9e9a)"></div><div class="name">LOREM IPSUM IS SIMPLY DUMMY</div><div class="link">Click here for view details</div></div>

<div class="rule" style="top:957px"></div>

<footer>
  <div class="foot-h" style="left:109px">WELCOME</div>
  <ul class="foot-list" style="left:109px"><li>Auctions</li><li>Sell &amp; Buy</li><li>Specialists</li><li>Services</li><li>Inside</li></ul>

  <div class="foot-h" style="left:243px">INFORMATION</div>
  <ul class="foot-list" style="left:243px"><li>Terms &amp; Conditions</li><li>Privacy Policy</li><li>Disclaimer</li></ul>

  <div class="foot-h" style="left:418px">NEWSLETTER SIGNUP</div>
  <p class="foot-copy" style="left:418px;top:1013px;width:170px">Get our recent updates through your Email Id</p>
  <div class="email"><span>Enter your email id</span><svg width="7" height="10" viewBox="0 0 7 10"><path d="M1 1l4.5 4-4.5 4" fill="none" stroke="#555" stroke-width="1.5"/></svg></div>

  <div class="foot-h" style="left:668px">FOLLOW US</div>
  <p class="foot-copy" style="left:668px;top:1013px">Connect with our social netwrok</p>
  <div class="social" style="left:668px;top:1038px"><i style="background:#2f64b0"></i>: Friendwall</div>
  <div class="social" style="left:769px;top:1038px"><i style="background:#4fb6e6"></i>: Chirpline</div>
  <div class="social" style="left:668px;top:1079px"><i style="background:#d8262c"></i>: Pinboardly</div>
  <div class="social" style="left:769px;top:1079px"><i style="background:#1a7aa6"></i>: Careerlink</div>
</footer>

<div class="rule" style="top:1140px"></div>
<div class="copyright">© 2015. Corvanel Antique Auction. All rights reserved.</div>

</body>
</html>
```